Road Sign at our office 84 in X 48 in - Small Billboard

Kestrel Electrical
Electrical & Lighting Services

- we need a sign design for our small business/company based in Calhoun, GA called Kestrel Electrical - "our mission is to provide Northwest Georgia with dependable, high-quality electrical services that prioritize safety, integrity, and long-term reliability. As a woman-owned business with over 25 years of experience, we are committed to delivering exceptional workmanship and personalized service for every commercial, residential, and industrial project we undertake. We stand behind our work with a lifetime warranty—because your trust is our most powerful connection."

display logo, phone number, and open to other ideas without being cluttered, maybe instead of full website address, just use @ksrelectrical and it will send them to all of our website and socials...

it needs to be easy to read as they drive down the road
this is a place where people may be traveling at high speeds, make sure it's easy to see and understand at a glance.
It will be hanging 20-24ft from the ground. Like a small billboard.

https://ksrelectricworks.com/

Industry/Entity Type

Electrical Contractor

Requirements
Nice to have
• match the look and feel of website and socials

```html
<!DOCTYPE html>
<html lang="en">
<head>
<meta charset="utf-8">
<title>Kestrel Electrical – Road Sign</title>
<link rel="stylesheet" href="https://fonts.googleapis.com/css2?family=Montserrat:wght@500;600;700&display=swap">
<style>
  :root {
    --page-bg: #eef0f3;
    --sign-dark: #120d0a;
    --sign-brown: #3a2212;
    --brand-red: #e8352e;
    --flame-orange: #ee5a2b;
    --flame-yellow: #f5b21b;
    --text-white: #ffffff;
    --flourish: rgba(150, 80, 20, 0.45);
  }
  * { margin: 0; padding: 0; box-sizing: border-box; }
  html, body {
    width: 1000px; height: 1200px; overflow: hidden;
    background: var(--page-bg);
    font-family: "Montserrat", Arial, sans-serif;
  }
  .road-sign {
    position: absolute; left: 20px; top: 326px;
    width: 960px; height: 548px; overflow: hidden;
    background: linear-gradient(180deg, var(--sign-dark) 0%, var(--sign-brown) 100%);
  }
  .brand-flourish {
    position: absolute; right: -40px; top: 120px;
    width: 260px; height: 440px; border-radius: 50% 0 0 50%;
    background: radial-gradient(ellipse at 70% 55%, var(--flourish) 0%, rgba(150,80,20,0.15) 55%, transparent 75%);
  }
  .brand-lockup { position: absolute; left: 44px; top: 48px; display: flex; align-items: center; gap: 22px; }
  .brand-dot { width: 96px; height: 96px; border-radius: 50%; background: var(--flame-orange); }
  .brand-name { color: var(--text-white); font-weight: 600; line-height: 1; }
  .brand-name .line-main { display: block; font-size: 66px; letter-spacing: -0.5px; }
  .brand-name .line-sub { display: block; font-size: 30px; letter-spacing: 8px; margin-top: 8px; }

  .headline-tag { position: absolute; left: 536px; top: 58px; display: flex; align-items: center; gap: 16px; }
  .headline-tag svg { width: 70px; height: 70px; }
  .headline-tag p {
    color: var(--brand-red); font-weight: 500; font-size: 24px; line-height: 1.25; text-transform: uppercase;
  }

  .service-list { position: absolute; left: 0; top: 210px; width: 100%; height: 110px; list-style: none; }
  .service { position: absolute; display: flex; flex-direction: column; align-items: flex-start; }
  .service-icon {
    width: 60px; height: 60px; border-radius: 50%;
    display: flex; align-items: center; justify-content: center;
  }
  .service-icon svg { width: 34px; height: 34px; }
  .service-icon.is-red { background: var(--flame-orange); }
  .service-icon.is-yellow { background: var(--flame-yellow); }
  .service-label {
    color: var(--text-white); font-weight: 500; font-size: 17px; text-transform: uppercase;
    margin-top: 16px; white-space: nowrap;
  }
  .service.lighting { left: 50px; } .service.lighting .service-icon { margin-left: 0; }
  .service.electrical { left: 278px; } .service.electrical .service-icon { margin-left: 0; }
  .service.security { left: 524px; } .service.security .service-icon { margin-left: 0; }
  .service.commercial { left: 778px; }

  .experience {
    position: absolute; left: 0; width: 100%; top: 340px; text-align: center;
    color: var(--text-white); font-weight: 600; font-size: 40px;
  }
  .social-handle {
    position: absolute; left: 0; width: 100%; top: 390px; text-align: center;
    color: var(--brand-red); font-weight: 600; font-size: 40px;
  }
  .phone-band {
    position: absolute; left: 0; bottom: 0; width: 100%; height: 98px;
    background: var(--brand-red);
    display: flex; align-items: center; justify-content: center; gap: 30px;
  }
  .phone-band svg { width: 52px; height: 52px; }
  .phone-number { color: var(--text-white); font-weight: 600; font-size: 80px; letter-spacing: 1px; line-height: 1; }
</style>
</head>
<body>
  <main class="road-sign">
    <div class="brand-flourish" role="img" aria-label="Faint flame-coloured brand decoration"></div>

    <div class="brand-lockup">
      <div class="brand-dot"></div>
      <h1 class="brand-name"><span class="line-main">Kestrel</span><span class="line-sub">Electrical</span></h1>
    </div>

    <div class="headline-tag">
      <svg viewBox="0 0 70 70" fill="none" stroke="#e8352e" stroke-width="2.5" stroke-linecap="round" stroke-linejoin="round">
        <circle cx="35" cy="35" r="32"/>
        <path d="M25 18v10M45 18v10"/>
        <path d="M20 28h30v8a15 15 0 0 1-30 0z"/>
        <path d="M37 32l-5 7h6l-5 7"/>
        <path d="M35 51v9"/>
      </svg>
      <p>Comprehensive<br>Electrical Services</p>
    </div>

    <ul class="service-list">
      <li class="service lighting">
        <span class="service-icon is-red">
          <svg viewBox="0 0 34 34" fill="none" stroke="#fff" stroke-width="1.8" stroke-linecap="round">
            <path d="M12 20a8 8 0 1 1 10 0v3H12z"/><path d="M13 26h8M14 29h6"/>
            <path d="M17 3V1M6 8L4 6M28 8l2-2M3 15H1M31 15h2"/>
          </svg>
        </span>
        <span class="service-label">Lighting Services</span>
      </li>
      <li class="service electrical">
        <span class="service-icon is-yellow">
          <svg viewBox="0 0 34 34" fill="none" stroke="#fff" stroke-width="1.8" stroke-linecap="round" stroke-linejoin="round">
            <path d="M13 4v6M21 4v6M9 10h16v6a8 8 0 0 1-16 0z"/><path d="M18 13l-3 4h4l-3 4"/><path d="M17 24v7"/>
          </svg>
        </span>
        <span class="service-label">Electrical Services</span>
      </li>
      <li class="service security">
        <span class="service-icon is-yellow">
          <svg viewBox="0 0 34 34" fill="none" stroke="#fff" stroke-width="1.8" stroke-linecap="round" stroke-linejoin="round">
            <path d="M4 15L17 5l13 10"/><path d="M7 13v16h20V13"/><rect x="12" y="17" width="10" height="8" rx="1"/><path d="M14 17v-2a3 3 0 0 1 6 0v2"/>
          </svg>
        </span>
        <span class="service-label">Electrical Segurity</span>
      </li>
      <li class="service commercial">
        <span class="service-icon is-red">
          <svg viewBox="0 0 34 34" fill="none" stroke="#fff" stroke-width="1.8" stroke-linecap="round">
            <path d="M12 20a8 8 0 1 1 10 0v3H12z"/><path d="M13 26h8M14 29h6"/>
            <path d="M19 11h-3a1.5 1.5 0 0 0 0 3h2a1.5 1.5 0 0 1 0 3h-3M17 9v2M17 17v2"/>
          </svg>
        </span>
        <span class="service-label">Commercial</span>
      </li>
    </ul>

    <p class="experience">over 25 years of experience</p>
    <p class="social-handle">@ksrelectrical</p>

    <div class="phone-band">
      <svg viewBox="0 0 24 24" fill="#fff">
        <path d="M6.6 10.8a15.1 15.1 0 0 0 6.6 6.6l2.2-2.2a1 1 0 0 1 1-.25 11.4 11.4 0 0 0 3.6.57 1 1 0 0 1 1 1V20a1 1 0 0 1-1 1A17 17 0 0 1 3 4a1 1 0 0 1 1-1h3.5a1 1 0 0 1 1 1c0 1.25.2 2.45.57 3.57a1 1 0 0 1-.25 1z"/>
      </svg>
      <span class="phone-number">706-555-0148</span>
    </div>
  </main>
</body>
</html>
```